Brightmere Realty information card

We need a 5x7 two-sided card to hand out at open houses and provide to our charitable partners for distribution. We are a local real estate group looking to add a "give back" component to our business. We are located in a coastal community and would like to incorporate that feel into our design. We are giving clients who use us the ability to designate 1 out of the 10 charitable organizations we partner with - and we will make a donation to that organization.

We included the 10 partner logos below - we envision them pretty small. Also included 2 photos of the "Brightmere" and our logo. Have fun.
Updates

Project Deadline Extended
Reason: We're out of town until Wednesday, May 17th.

Target Market(s)

home buyers & sellers

Industry/Entity Type

Real Estate

Font styles to use
Serif
Sans Serif

Colors

Designer to choose colors to be used in the design.

Requirements
Must have
• slogan & tagline - see attached text file
• Brightmere photo
Nice to have
• partner logos - small - maybe in circles?

```html
<!DOCTYPE html>
<html lang="en">
<head>
<meta charset="utf-8">
<title>Brightmere Realty – Information Card</title>
<link href="https://fonts.googleapis.com/css2?family=Josefin+Sans:wght@400;600&family=Raleway:wght@400;500;600&display=swap" rel="stylesheet">
<style>
  :root {
    --ink: #111111;
    --paper: #ffffff;
    --brand-blue: #5b8ac9;
    --brand-blue-dark: #3f6aa6;
    --url-ink: #1b2236;
    --sky-top: #7683a6;
    --sky-rose: #d8868c;
    --sky-glow: #ea8d6f;
    --horizon: #f0a286;
    --sea: #cc8a86;
    --shore: #7d5a5e;
    --town: #463a42;
    --town-deep: #2a2327;
  }
  * { margin: 0; padding: 0; box-sizing: border-box; }
  html, body { width: 857px; height: 1200px; overflow: hidden; background: var(--paper); }
  .card { position: relative; width: 857px; height: 1200px; overflow: hidden; background: var(--paper); }

  .hero-photo {
    position: absolute; left: 0; top: 0; width: 857px; height: 835px;
    background: linear-gradient(180deg,
      var(--sky-top) 0%,
      #a88598 9%,
      var(--sky-rose) 18%,
      var(--sky-glow) 32%,
      var(--horizon) 44%,
      #e29b88 49.5%,
      var(--sea) 51%,
      #c78680 59%,
      var(--shore) 64%,
      var(--town) 72%,
      #3a3036 86%,
      var(--town-deep) 100%);
  }

  .brand-block {
    position: absolute; left: 120px; top: 0; width: 322px; height: 350px;
    background: var(--ink);
    display: flex; flex-direction: column; align-items: center; justify-content: center;
    padding-top: 90px;
  }
  .brand-name {
    font-family: 'Raleway', sans-serif; font-weight: 600;
    color: var(--paper); font-size: 52px; line-height: 1.25; text-align: center;
  }

  .headline {
    position: absolute; left: 461px; top: 40px;
    font-family: 'Josefin Sans', sans-serif; font-weight: 400;
    color: var(--paper); font-size: 62px; line-height: 61px; letter-spacing: 0;
    text-transform: uppercase;
  }
  .tagline {
    position: absolute; left: 463px; top: 290px;
    font-family: 'Raleway', sans-serif; font-weight: 400;
    color: var(--paper); font-size: 22px; line-height: 30px; letter-spacing: 0.2px;
  }

  .giving-statement { position: absolute; left: 57px; top: 884px; width: 760px; }
  .giving-statement h2 {
    font-family: 'Josefin Sans', sans-serif; font-weight: 600;
    font-size: 29px; line-height: 40px; letter-spacing: 1.8px;
    text-transform: uppercase; color: var(--ink);
  }
  .giving-statement p {
    margin-top: 18px;
    font-family: 'Raleway', sans-serif; font-weight: 500;
    font-size: 21px; line-height: 29px; color: var(--ink);
  }

  .footer-band { position: absolute; left: 0; top: 1135px; width: 857px; height: 65px; background: var(--ink); }
  .url-tab { position: absolute; left: 340px; top: 1103px; width: 470px; height: 80px; }
  .url-text {
    position: absolute; left: 408px; top: 1125px;
    font-family: 'Raleway', sans-serif; font-weight: 500;
    font-size: 25px; color: var(--url-ink);
  }
</style>
</head>
<body>
<main class="card">
  <div class="hero-photo" role="img" aria-label="Coastal town at dusk under a pink and orange sunset sky, with a curving bay, beach, pier and lit streets below"></div>

  <div class="brand-block">
    <div class="brand-name">Brightmere<br>Realty</div>
  </div>

  <h1 class="headline">Change<br>Homes,<br>Change<br>Lives</h1>
  <p class="tagline">Changing the World One<br>Home at a Time</p>

  <section class="giving-statement">
    <h2>Because we value generosity and desire<br>to make a difference in our community<br>and world,</h2>
    <p>for every home bought or sold through us, we will make a contribution<br>to one of our amazing partner who are helping to change the world.</p>
  </section>

  <div class="footer-band"></div>
  <svg class="url-tab" viewBox="0 0 470 80" aria-hidden="true">
    <polygon points="22,0 440,0 470,80 0,80" fill="var(--brand-blue)"/>
    <polygon points="22,0 40,0 20,34 2,34" fill="var(--brand-blue-dark)"/>
  </svg>
  <a class="url-text">www.brightmererealty.com</a>
</main>
</body>
</html>
```